we need a business card as well as a logo that can be used for signs etc.
this is a very formal, classy , elegant function centre, as well as café. I am after a design that stands out and grabs people attentions. my colours theme is really warm ,colours like chocolate browns, and latte type colours with really deep red tones
not bright red, just warm tones. this is a place that very wealthy and maybe even celebs will come so I need it to be appealing.
Industry/Entity Type
Business
Contact Information for Business Card
Blue Fern
café and function centre @ hallam orchard.
wedding and function specialists,
Barrow parkway, lucknow,ph 0438157240

```html
<!DOCTYPE html>
<html lang="en">
<head>
<meta charset="utf-8">
<title>Blue Fern – business card</title>
<link rel="stylesheet" href="https://fonts.googleapis.com/css2?family=Michroma&family=Cabin:wght@400&display=swap">
<style>
  :root {
    --backdrop: #1a1a1a;
    --card-brown: #7a5d56;
    --band-brown: #6a4c45;
    --band-light: #8a6d66;
    --ribbon-latte: #b59d93;
    --ribbon-soft: #957a72;
    --leaf-faint: #86665f;
    --text-cream: #f1e6df;
    --deep-red: #6b1015;
    --mark-ring: #8c716a;
  }
  * { margin: 0; padding: 0; box-sizing: border-box; }
  html, body {
    width: 1200px; height: 1000px; overflow: hidden;
    background: var(--backdrop);
  }
  .canvas { position: relative; width: 1200px; height: 1000px; }
  .business-card {
    position: absolute; left: 120px; top: 235px;
    width: 960px; height: 530px;
    background: var(--card-brown);
    clip-path: polygon(24px 0, 100% 0, 100% 100%, 0 100%, 0 24px);
    overflow: hidden;
  }
  .name-band {
    position: absolute; left: 0; top: 80px; width: 100%; height: 60px;
    background: linear-gradient(90deg, var(--band-brown) 0%, var(--band-brown) 55%, var(--band-light) 100%);
  }
  .leaf-scatter {
    position: absolute; left: 620px; top: 40px; width: 340px; height: 260px;
    background: radial-gradient(ellipse at 60% 45%, var(--leaf-faint) 0%, rgba(134,102,95,0) 70%);
  }
  .ribbon-area {
    position: absolute; left: 0; top: 320px; width: 960px; height: 100px;
    background: linear-gradient(180deg,
      rgba(149,122,114,0) 0%,
      var(--ribbon-soft) 30%,
      var(--ribbon-latte) 55%,
      var(--ribbon-soft) 80%,
      rgba(149,122,114,0) 100%);
    opacity: .75;
  }
  .mark-circle {
    position: absolute; left: 38px; top: 334px;
    width: 156px; height: 156px; border-radius: 50%;
    background: var(--deep-red);
    border: 4px solid var(--mark-ring);
  }
  .hang-hole {
    position: absolute; left: 848px; top: 38px;
    width: 36px; height: 36px; border-radius: 50%;
    background: var(--backdrop);
  }
  .brand-name {
    position: absolute; left: 120px; top: 90px;
    font-family: "Michroma", sans-serif; font-size: 38px; font-weight: 400;
    line-height: 1; letter-spacing: 2px; color: var(--text-cream);
  }
  .tagline {
    position: absolute; left: 120px; top: 150px;
    font-family: "Cabin", sans-serif; font-size: 29px; color: var(--text-cream);
  }
  .venue-line {
    position: absolute; left: 120px; top: 194px;
    font-family: "Cabin", sans-serif; font-size: 19px; color: var(--text-cream);
  }
  .contact {
    position: absolute; left: 560px; top: 436px;
    font-family: "Cabin", sans-serif; font-size: 25px; line-height: 38px;
    color: var(--text-cream);
  }
</style>
</head>
<body>
<main class="canvas">
  <section class="business-card">
    <div class="name-band"></div>
    <div class="leaf-scatter" role="img" aria-label="faint scattered autumn leaves"></div>
    <div class="ribbon-area" role="img" aria-label="flowing latte ribbons across the card"></div>
    <div class="mark-circle"></div>
    <div class="hang-hole"></div>
    <h1 class="brand-name">Blue Fern</h1>
    <p class="tagline">café and function centre</p>
    <p class="venue-line">@ hallam orchard. wedding and function specialists,</p>
    <p class="contact">Barrow parkway, lucknow,<br>ph 0438157240</p>
  </section>
</main>
</body>
</html>
```